Plakate für ein Malereibetreib
Zielgruppe
Wir sind ein familiär geführter Malereibetreib (7 Mitarbeiter) mit Aufträgen in den Gewerken Fassadenrenovierungen und Balkonabdichtung.
Wir sind auf der Suche nach kräftigen, arbeitswilligen Mitarbeiter, die Freude daran haben, mit Ihren Händen, mehrheitlich draussen zu arbeiten und dafür gut bezahlt werden.
Aufgabenstellung
Das Plakat wird auf eine Fassade mit direktem Blick von einem großen Supermarktparkplatz montiert.
Die Größe wird ca. 4m x 4 m betragen.
Wir möchten unser Plakat NICHT im Stil unserer Homepage gestaltet haben. Die ist uns für den Zweck der Mitarbeitersuche zu brav.
Ebenso bitte KEINE 'klassischen' Stock-Bilder (Malerpinsel, bunte Farbdosen, angeschmierte Leitern) verwendet werden.
Das Plakat soll eher ohne Fotos, sondern lieber mit Grafiken (Comic, Zeichnungen...) gestaltet sein.
Es soll zum witzigen, spontanen, sehr auffallenden, kurzzeitigen Aufruf nach Fachkräften für unseren Betrieb dienen.
Uns gefallen Retro-Schriften sehr gut.
Als Kontaktdaten soll auf dem Plakat nur unser Firmenname 'brolting', Telefonnummer 089 52 17 63 und Website www.brolting-gmbh.de stehen.

```html
<!DOCTYPE html>
<html lang="de">
<head>
<meta charset="utf-8">
<title>brolting – Wir suchen Fachkräfte</title>
<link rel="stylesheet" href="https://fonts.googleapis.com/css2?family=Rubik+Dirt&family=Questrial&family=Nunito:wght@700&display=swap">
<style>
  :root {
    --poster-red: #e2503b;
    --cream: #f6e4c4;
    --olive: #3f4530;
    --band-white: #ffffff;
    --accent-orange: #e5741f;
  }
  * { margin: 0; padding: 0; box-sizing: border-box; }
  html, body {
    width: 1200px;
    height: 800px;
    overflow: hidden;
    background: var(--poster-red);
  }
  .poster {
    position: relative;
    width: 1200px;
    height: 800px;
    background: var(--poster-red);
    overflow: hidden;
  }
  .brush-stroke {
    position: absolute;
    left: 890px;
    top: 240px;
    width: 130px;
    height: 530px;
    z-index: 2;
  }
  .headline {
    position: absolute;
    left: 82px;
    top: 90px;
    font-family: "Rubik Dirt", "Impact", sans-serif;
    font-weight: 400;
    font-size: 90px;
    line-height: 1.28;
    color: var(--cream);
    text-transform: uppercase;
    letter-spacing: 1px;
    z-index: 3;
  }
  .headline .highlight { color: var(--olive); }
  .website {
    position: absolute;
    left: 86px;
    top: 555px;
    font-family: "Questrial", "Century Gothic", sans-serif;
    font-size: 50px;
    color: var(--cream);
    letter-spacing: 1px;
    z-index: 3;
  }
  .info-band {
    position: absolute;
    left: 0;
    bottom: 0;
    width: 1200px;
    height: 112px;
    background: var(--band-white);
    z-index: 1;
  }
  .info-band .callout,
  .info-band .phone {
    position: absolute;
    font-family: "Nunito", "Century Gothic", sans-serif;
    font-weight: 700;
    font-size: 20px;
    color: var(--accent-orange);
  }
  .info-band .callout { left: 86px; top: 28px; }
  .info-band .phone { left: 520px; top: 62px; }
  .brand {
    position: absolute;
    right: 40px;
    bottom: 26px;
    display: flex;
    align-items: center;
    gap: 10px;
    font-family: "Nunito", "Century Gothic", sans-serif;
    font-weight: 700;
    font-size: 24px;
    color: var(--olive);
    z-index: 3;
  }
  .brand .brand-square {
    width: 16px;
    height: 16px;
    background: var(--olive);
  }
</style>
</head>
<body>
  <main class="poster">
    <h1 class="headline">„Den Rest<br>macht dann<br>die <span class="highlight">Farbe.“</span></h1>
    <p class="website">www.brolting-gmbh.de</p>

    <svg class="brush-stroke" viewBox="0 0 130 530" role="img" aria-label="Breiter olivgrüner Pinselstrich von oben nach unten">
      <rect x="0" y="0" width="130" height="530" fill="var(--olive)"/>
    </svg>

    <footer class="info-band">
      <p class="callout">Wir suchen Fachkräfte!</p>
      <p class="phone">Tel.: +49 089 52 17 63</p>
    </footer>

    <div class="brand">
      <span class="brand-square"></span>
      <span class="brand-name">brolting</span>
    </div>
  </main>
</body>
</html>
```